Flyer Mail out

Need something urgently designed.

I need a flyer done double sided I have provided KTHS photos and the writing. I do not have any dental surgery stock photos as such but this can be used. We are a mobile dental company that goes out to schools and provide free dental services.

I have attached the written document and would like it double sided A4 paper.

The colours I want is Aqua, Light Blue, dark blue, grey and white.

Just need it designed beautifully and professionally to go out to principals to contact us and use our services.

If you would like more info have a look at our Friendbook page Kestrel Travelling Health Smiles

```html
<!DOCTYPE html>
<html lang="en">
<head>
<meta charset="utf-8">
<title>KTHS Flyer</title>
<link href="https://fonts.googleapis.com/css2?family=Bebas+Neue&family=Roboto+Condensed:wght@400;700&family=Tinos&display=swap" rel="stylesheet">
<style>
:root{
  --sky-top:#7fb3dc;
  --sky-bottom:#c9def0;
  --scrub:#1e3f9c;
  --aqua:#1b9ad8;
  --navy:#1f3c86;
  --orange:#ef7d1b;
  --magenta:#e2227c;
  --ink:#222;
  --white:#fff;
  --clinic:#dfe3e4;
}
*{margin:0;padding:0;box-sizing:border-box}
html,body{width:927px;height:1200px;overflow:hidden;background:var(--white)}
.flyer{position:relative;width:927px;height:1200px;overflow:hidden;background:var(--white);font-family:"Roboto Condensed",sans-serif;color:var(--ink)}
.hero-photo{position:absolute;left:0;top:0;width:927px;height:530px;
  background:linear-gradient(180deg,var(--sky-top) 0%,var(--sky-bottom) 55%,var(--scrub) 56%,var(--scrub) 100%);
  clip-path:polygon(0 0,100% 0,100% 100%,52% 100%,43% 468px,0 468px)}
.team-photo{position:absolute;left:597px;top:278px;width:310px;height:364px;border:8px solid var(--white);border-radius:14px;
  background:linear-gradient(180deg,#f1f3f4 0%,var(--clinic) 60%,#b9d5dc 100%);box-shadow:0 2px 8px rgba(0,0,0,.35)}
.headline{position:absolute;left:28px;top:488px;font-family:"Bebas Neue",sans-serif;font-size:68px;line-height:62px;letter-spacing:.5px}
.headline .line1{color:var(--aqua);display:block}
.headline .line2{color:var(--navy);display:block}
.quote{position:absolute;left:40px;width:850px;top:656px;text-align:center;font-family:"Tinos",serif;font-size:24.5px;line-height:28px;color:var(--ink)}
.quote-ref{position:absolute;right:108px;top:712px;font-family:"Tinos",serif;font-size:12.5px;color:var(--ink)}
.body-copy{position:absolute;left:40px;width:850px;top:732px;text-align:center;font-size:19px;line-height:29px;color:var(--ink)}
.cta-book{position:absolute;left:20px;top:788px;font-family:"Bebas Neue",sans-serif;font-size:50px;color:var(--orange);letter-spacing:.3px}
.cta-bring{position:absolute;left:243px;top:868px;font-family:"Bebas Neue",sans-serif;font-size:37px;color:var(--aqua)}
.cta-smile{position:absolute;left:595px;top:838px;font-family:"Bebas Neue",sans-serif;font-size:64px;color:var(--magenta)}
.contact-band{position:absolute;left:0;top:962px;width:927px;height:238px;background:var(--aqua)}
.band-art{position:absolute;left:0;top:962px}
.contact{position:absolute;top:932px;width:220px;text-align:center;color:var(--white)}
.contact .icon{display:block;margin:0 auto;width:74px;height:74px}
.contact .value{display:block;margin-top:3px;font-weight:700;font-size:17px}
.contact .label{display:block;margin-top:6px;font-size:18px;color:#0d1b2a}
.social{position:absolute;top:1087px;width:82px;height:82px;border-radius:50%;background:var(--white);border:4px solid var(--aqua);
  display:flex;align-items:center;justify-content:center;font-weight:700;font-size:13px;color:var(--aqua)}
.footer-note{position:absolute;left:0;width:927px;top:1163px;text-align:center;color:var(--white);font-size:17px}
</style>
</head>
<body>
<div class="flyer">
  <div class="hero-photo" role="img" aria-label="Photo of three smiling dental staff in navy scrubs against a blue sky"></div>
  <div class="team-photo" role="img" aria-label="Photo of two smiling dental clinicians in a treatment room"></div>

  <h1 class="headline"><span class="line1">“Our focus is on</span><span class="line2">Education &amp; Prevention”</span></h1>

  <p class="quote">“1 in 5 children between the ages of 4-8 years of age will suffer from tooth decay or dental caries as a result of poor dental hygiene”</p>
  <p class="quote-ref">(ref; The Southern College of Child Health)</p>
  <p class="body-copy">Thus, leading to possible dental destruction to their adult teeth. This, in conjunction with diet, lifestyle and social welfare can be contribution to the increase of child absenteeism.</p>

  <p class="cta-book">Book us now for 2015 and help us,</p>
  <p class="cta-bring">Bring back your student's</p>
  <p class="cta-smile">“Bright Smile”</p>

  <div class="contact-band"></div>
  <svg class="band-art" width="927" height="238" viewBox="0 0 927 238">
    <path d="M0 132 C90 128 150 104 230 102 L700 102 C780 104 840 128 927 132" fill="none" stroke="#fff" stroke-width="2"/>
  </svg>

  <div class="contact" style="left:137px">
    <svg class="icon" viewBox="0 0 74 74"><circle cx="37" cy="37" r="34" fill="#fff" stroke="#1b9ad8" stroke-width="4"/>
      <g fill="none" stroke="#111" stroke-width="2.2"><circle cx="37" cy="37" r="16"/><ellipse cx="37" cy="37" rx="7" ry="16"/><path d="M21 37h32M23 29h28M23 45h28M37 21v32"/></g></svg>
    <span class="value">www.kths.net.au</span>
    <span class="label">Please Visit Our Website</span>
  </div>
  <div class="contact" style="left:354px">
    <svg class="icon" viewBox="0 0 74 74"><circle cx="37" cy="37" r="34" fill="#fff" stroke="#1b9ad8" stroke-width="4"/>
      <g fill="none" stroke="#111" stroke-width="2.2"><rect x="21" y="27" width="32" height="21"/><path d="M21 27l16 13 16-13M21 48l12-11M53 48l-12-11"/></g></svg>
    <span class="value">Marla.t@kths.net.au</span>
    <span class="label">E-mail to Us</span>
  </div>
  <div class="contact" style="left:570px">
    <svg class="icon" viewBox="0 0 74 74"><circle cx="37" cy="37" r="34" fill="#fff" stroke="#1b9ad8" stroke-width="4"/>
      <circle cx="37" cy="37" r="17" fill="none" stroke="#111" stroke-width="2.2"/>
      <path d="M31 26c-3 2-4 6-2 11s6 10 10 12c3 1 5 0 6-2l-4-4-3 2c-2-1-5-5-6-8l2-3z" fill="#111"/></svg>
    <span class="value">(02) 5550 1274</span>
    <span class="label">Speak to Friendly Staff</span>
  </div>

  <div class="social" style="left:322px">Chatter</div>
  <div class="social" style="left:428px">Friendbook</div>
  <div class="social" style="left:543px">Linkwork</div>

  <p class="footer-note">Visit to see Regular Updates, Features, Special Offers &amp; Daily Tips Regarding our Services.</p>
</div>
</body>
</html>
```